New Years Greeting Card Design Competition

We need a greeting card design for the new year 2014. We would like to have pictures of our daughter Meera on the card. Please find attached 5 photos of her. Please feel free to use all 5 or some of them for the design. We would like the following text on the card: "Happy New Year" and "Vik, Pooja, and Meera Deshpande." We would like to see designs that are very positive in style.

Target Market(s)

The greeting card is going to be sent to family and friends in different parts of the world.

Requirements
Must have
• We would like to have pictures of our daughter Meera on the card. Please find attached 5 photos of her. Please feel free to use all 5 or some of them for the design. We would like the following text on the card: "Happy New Year" and "Vik, Pooja, and Meera Deshpande."

```html
<!DOCTYPE html>
<html lang="en">
<head>
<meta charset="utf-8">
<title>Happy New Year 2014 – Vik, Pooja, and Meera Deshpande</title>
<link rel="stylesheet" href="https://fonts.googleapis.com/css2?family=Caveat:wght@500;600&family=Delius&display=swap">
<style>
  :root {
    --night: #000000;
    --spark: #c9c98a;
    --spark-dim: #5f5f3c;
    --ink: #fbfaf2;
    --shadow: rgba(0, 0, 0, 0.75);
    --photo-pink: #e58aa6;
    --photo-cloth: #cfd9dc;
  }
  html, body {
    margin: 0;
    padding: 0;
    overflow: hidden;
    background: var(--night);
  }
  .card {
    position: relative;
    width: 1200px;
    height: 900px;
    overflow: hidden;
    background: var(--night);
  }
  .fireworks-backdrop {
    position: absolute;
    inset: 0;
    background:
      radial-gradient(circle at 880px 260px, var(--spark) 0, rgba(201, 201, 138, 0.75) 90px, rgba(150, 150, 95, 0.45) 230px, rgba(0, 0, 0, 0) 360px),
      radial-gradient(ellipse 220px 260px at 760px 760px, rgba(95, 95, 60, 0.55), rgba(0, 0, 0, 0) 100%),
      radial-gradient(ellipse 260px 220px at 330px 240px, rgba(95, 95, 60, 0.35), rgba(0, 0, 0, 0) 100%),
      var(--night);
  }
  .greeting {
    position: absolute;
    left: 80px;
    top: 72px;
    margin: 0;
    font-family: "Caveat", cursive;
    font-weight: 500;
    font-size: 76px;
    line-height: 1;
    color: var(--ink);
    text-shadow: 2px 3px 4px var(--shadow);
  }
  .year-digit {
    position: absolute;
    font-family: "Caveat", cursive;
    font-weight: 500;
    font-size: 440px;
    line-height: 1;
    color: var(--ink);
    text-shadow: 2px 4px 6px var(--shadow);
  }
  .year-two { left: 56px; top: 200px; }
  .year-rest { left: 745px; top: 188px; letter-spacing: -10px; }
  .portrait-heart {
    position: absolute;
    left: 350px;
    top: 262px;
    width: 397px;
    height: 355px;
  }
  .family-names {
    position: absolute;
    left: 450px;
    top: 700px;
    margin: 0;
    font-family: "Delius", sans-serif;
    font-size: 52px;
    line-height: 64px;
    color: var(--ink);
    text-shadow: 2px 3px 4px var(--shadow);
  }
</style>
</head>
<body>
  <main class="card">
    <div class="fireworks-backdrop" role="img" aria-label="Photograph of a golden firework burst against the night sky"></div>

    <h1 class="greeting">Happy New Year</h1>

    <span class="year-digit year-two" aria-hidden="true">2</span>
    <svg class="portrait-heart" viewBox="0 0 400 360" role="img" aria-label="Heart-shaped photo of baby Meera in a pink outfit lying on a patterned blanket">
      <defs>
        <linearGradient id="heart-fill" x1="0" y1="0" x2="1" y2="1">
          <stop offset="0" stop-color="var(--photo-cloth)"/>
          <stop offset="0.55" stop-color="var(--photo-pink)"/>
          <stop offset="1" stop-color="var(--photo-cloth)"/>
        </linearGradient>
      </defs>
      <path fill="url(#heart-fill)" d="M200 358 C150 290 0 232 0 110 C0 40 50 0 105 0 C150 0 185 25 200 60 C215 25 250 0 295 0 C350 0 400 40 400 110 C400 232 250 290 200 358 Z"/>
    </svg>
    <span class="year-digit year-rest" aria-hidden="true">14</span>
    <span class="visually-year" style="position:absolute;width:1px;height:1px;overflow:hidden;clip:rect(0 0 0 0);">2014</span>

    <p class="family-names">Vik, Pooja, and Meera<br>Deshpande</p>
  </main>
</body>
</html>
```